Larkfield letterhead design and business card design for electrical company

I need a letterhead that can be used for my invoices and quote books along with emails sent to clients. I have a logo and the logo of Trade Wirecraft Guild I just need all my information placed nicely with a good flow.

Business Name: Larkfield Electrical
Name: Daniel Korvenith
Abn: 58906412375
Licence Number: 37419
Number: 0400583064

Thank you in advanced

Target Market(s)

Electrical Clients

Industry/Entity Type

Business

Contact Information for Business Card

Name: Daniel Korvenith
Abn: 58906412375
Licence Number: 37419
Number: 0400583064

Font styles to use
Sans Serif

Colors

Designer to choose colors to be used in the design.

Requirements
Must have
• Must have my logo, trade wirecraft guild logo even if its smaller and in the corner and all details
Nice to have
• Domestic Commercial Industrial stated on there somewhere

```html
<!DOCTYPE html>
<html lang="en">
<head>
<meta charset="utf-8">
<title>Larkfield Electrical – Stationery</title>
<link href="https://fonts.googleapis.com/css2?family=Open+Sans:wght@400;600;700&display=swap" rel="stylesheet">
<style>
  :root{
    --bg:#e0e0e0;
    --paper:#ffffff;
    --blue:#1b4f9c;
    --blue-deep:#123e86;
    --blue-light:#2f7fd0;
    --grey-stripe:#3a3a3c;
    --ink:#222426;
    --badge:#1c3b2c;
    --card-black:#050505;
  }
  *{margin:0;padding:0;box-sizing:border-box}
  html,body{width:1200px;height:1000px;overflow:hidden;background:var(--bg)}
  body{position:relative;font-family:"Open Sans",Arial,sans-serif;color:var(--ink)}
  .sheet{position:absolute;background:var(--paper);box-shadow:0 2px 4px rgba(0,0,0,.25)}
  .brand{font-family:"Open Sans",Arial,sans-serif;font-weight:700;color:var(--blue);line-height:1.1;white-space:nowrap}
  .brand-mark{display:inline-block;background:var(--blue);border-radius:50%;flex:none}
  .footer-wave{position:absolute;left:0;bottom:0;width:100%}
  .footer-text{position:absolute;color:#fff;font-weight:600;white-space:nowrap}

  /* letterhead */
  .letterhead{left:81px;top:168px;width:515px;height:668px}
  .letterhead .logo{position:absolute;left:32px;top:52px;display:flex;gap:8px;align-items:center}
  .letterhead .logo .brand-mark{width:16px;height:16px}
  .letterhead .logo .brand{font-size:22px}
  .contact-block{position:absolute;left:378px;top:42px;border-left:1px solid #555;padding-left:6px;font-size:8px;line-height:10px;white-space:nowrap}
  .contact-block .gap{height:6px}
  .contact-block .row{display:flex;align-items:center;gap:4px}
  .icon{width:7px;height:7px;flex:none}
  .guild{position:absolute;display:flex;align-items:center;gap:4px}
  .guild .badge{background:var(--badge);flex:none}
  .guild .label{font-weight:700;color:#1f3350;text-transform:uppercase;line-height:1.1}
  .letterhead .guild{left:32px;top:614px}
  .letterhead .guild .badge{width:21px;height:23px}
  .letterhead .guild .label{font-size:7px;width:72px}
  .letterhead .footer-text{right:28px;bottom:9px;font-size:7px}

  /* business card */
  .card-front{left:627px;top:168px;width:214px;height:125px}
  .card-front .logo{position:absolute;left:14px;top:18px;display:flex;gap:4px;align-items:center}
  .card-front .logo .brand-mark{width:8px;height:8px}
  .card-front .logo .brand{font-size:10px}
  .card-front .guild{left:150px;top:16px}
  .card-front .guild .badge{width:12px;height:13px}
  .card-front .guild .label{font-size:4.4px;width:48px}
  .person{position:absolute;left:11px;top:63px;font-size:5px;line-height:7px;white-space:nowrap}
  .person .name{font-size:7px;font-weight:700;color:var(--blue)}
  .person .role{font-weight:600;margin-bottom:3px}
  .person .blue{color:var(--blue);font-weight:600}
  .person .row{display:flex;align-items:center;gap:3px}
  .person .icon{width:4px;height:4px}
  .card-front .addr{position:absolute;right:10px;top:97px;font-size:5px;line-height:6px;text-align:right;white-space:nowrap}
  .card-front .footer-text{right:8px;bottom:2px;font-size:5px}
  .card-back{left:858px;top:168px;width:214px;height:125px;background:var(--card-black)}
  .card-back .logo{position:absolute;left:0;right:0;top:52px;display:flex;justify-content:center;align-items:center;gap:6px}
  .card-back .brand-mark{width:12px;height:12px;background:var(--blue-light)}
  .card-back .brand{font-size:15px;color:var(--blue-light)}

  /* envelope back */
  .env-back{left:627px;top:361px;width:489px;height:226px}
  .env-back svg{position:absolute;left:0;top:0}
  .env-back .logo{position:absolute;left:0;right:0;top:20px;display:flex;justify-content:center;align-items:center;gap:5px}
  .env-back .brand-mark{width:10px;height:10px;background:#fff}
  .env-back .brand{font-size:14px;color:#fff}
  .env-back .shade{position:absolute;left:0;bottom:0;width:100%;height:3px;background:#555}

  /* envelope front */
  .env-front{left:627px;top:610px;width:489px;height:226px}
  .env-front .logo{position:absolute;left:18px;top:36px;display:flex;gap:7px;align-items:center}
  .env-front .logo .brand-mark{width:13px;height:13px}
  .env-front .logo .brand{font-size:17px}
  .env-front .addr{position:absolute;left:18px;top:180px;font-size:7px;line-height:9px;white-space:nowrap}
  .env-front .footer-text{right:28px;bottom:8px;font-size:9px;font-weight:400}
</style>
</head>
<body>

<section class="sheet letterhead">
  <div class="logo"><span class="brand-mark"></span><span class="brand">Larkfield Electrical</span></div>
  <div class="contact-block">
    <div>55 demo street, demo place</div>
    <div>P.O. Box 000, 555 Avenue</div>
    <div class="gap"></div>
    <div class="row"><svg class="icon" viewBox="0 0 10 10"><path d="M2 1l2 2-1 1c1 2 2 3 3 3l1-1 2 2-1 1C4 9 1 6 1 2z" fill="#2f7fd0"/></svg>0400583064</div>
    <div class="row"><svg class="icon" viewBox="0 0 10 10"><rect x="1" y="2" width="8" height="6" fill="#2f7fd0"/><path d="M1 2l4 3 4-3" stroke="#fff" fill="none"/></svg>info@websitename.com</div>
    <div class="row"><svg class="icon" viewBox="0 0 10 10"><circle cx="5" cy="5" r="4" fill="none" stroke="#2f7fd0"/><path d="M1 5h8M5 1v8" stroke="#2f7fd0"/></svg>www.websitename.com</div>
  </div>
  <div class="guild"><span class="badge"></span><span class="label">Trade Wirecraft Guild Member</span></div>
  <svg class="footer-wave" width="515" height="30" viewBox="0 0 515 30" aria-hidden="true">
    <path d="M0 7H285C295 7 300 10 305 14H0z" fill="var(--grey-stripe)"/>
    <path d="M0 16H300C315 16 320 2 345 2H515V30H0z" fill="var(--blue)"/>
  </svg>
  <div class="footer-text">Abn: 58906412375 &nbsp;|&nbsp; Licence Number: 37419</div>
</section>

<section class="sheet card-front">
  <div class="logo"><span class="brand-mark"></span><span class="brand">Larkfield Electrical</span></div>
  <div class="guild"><span class="badge"></span><span class="label">Trade Wirecraft Guild Member</span></div>
  <div class="person">
    <div class="name">Daniel Korvenith</div>
    <div class="role">President</div>
    <div class="blue">Abn: 58906412375</div>
    <div class="blue">Licence Num: 37419</div>
    <div class="row"><svg class="icon" viewBox="0 0 10 10"><path d="M2 1l2 2-1 1c1 2 2 3 3 3l1-1 2 2-1 1C4 9 1 6 1 2z" fill="#2f7fd0"/></svg>0400583064</div>
    <div class="row"><svg class="icon" viewBox="0 0 10 10"><rect x="1" y="2" width="8" height="6" fill="#2f7fd0"/></svg>info@websitename.com</div>
  </div>
  <div class="addr">55 demo street, demo place<br>P.O. Box 000, 555 Avenue</div>
  <svg class="footer-wave" width="214" height="14" viewBox="0 0 214 14" aria-hidden="true">
    <path d="M0 3H120C128 3 131 5 134 7H0z" fill="var(--grey-stripe)"/>
    <path d="M0 8H130C140 8 142 1 155 1H214V14H0z" fill="var(--blue)"/>
  </svg>
  <div class="footer-text">www.websitename.com</div>
</section>

<section class="sheet card-back">
  <div class="logo"><span class="brand-mark"></span><span class="brand">Larkfield Electrical</span></div>
</section>

<section class="sheet env-back">
  <svg width="489" height="64" viewBox="0 0 489 64" aria-hidden="true">
    <defs>
      <linearGradient id="flap" x1="0" y1="0" x2="1" y2="1">
        <stop offset="0" stop-color="#123e86"/>
        <stop offset=".55" stop-color="#2f7fd0"/>
        <stop offset="1" stop-color="#123e86"/>
      </linearGradient>
    </defs>
    <path d="M0 0H489V40C489 56 482 62 470 62H20C8 62 0 56 0 40z" fill="url(#flap)"/>
  </svg>
  <div class="logo"><span class="brand-mark"></span><span class="brand">Larkfield</span></div>
  <div class="shade"></div>
</section>

<section class="sheet env-front">
  <div class="logo"><span class="brand-mark"></span><span class="brand">Larkfield Electrical</span></div>
  <div class="addr">55 demo street, demo place<br>P.O. Box 000, 555 Avenue</div>
  <svg class="footer-wave" width="489" height="26" viewBox="0 0 489 26" aria-hidden="true">
    <path d="M0 5H275C285 5 290 8 295 11H0z" fill="var(--grey-stripe)"/>
    <path d="M0 13H290C305 13 310 1 335 1H489V26H0z" fill="var(--blue)"/>
  </svg>
  <div class="footer-text">www.websitename.com</div>
</section>

</body>
</html>
```